Kneadwell Bodycare

We are a Massage Therapy business based in Invercargill, New Zealand. We specialise in Sports and deep tissue massage but also provide relaxation and aromatherapy massage. We would like to see designs that use the the logo.
The final design should promote health and fitness.
Updates

Hi I am getting feedback that my business card picture is poor quality. I got this picture from plaza press under massage. So if you google this image a better quality picture should come up,. If not hope to upload a better image by tomorow, thanks.

Target Market(s)

Sports, people with pain and injuries

Industry/Entity Type

Massage

Requirements
Must have
• Logo, muscle body that is used on the business card, also a poster that matches my business card
Nice to have
• Picture of muscle man, shown on my business card
Should not have
• Not a picture of a real person

```html
<!DOCTYPE html>
<html lang="en">
<head>
<meta charset="UTF-8">
<title>Kneadwell Bodycare – Poster</title>
<link rel="stylesheet" href="https://fonts.googleapis.com/css2?family=Open+Sans:wght@600;700&family=PT+Serif:ital,wght@0,400;0,700;1,400&display=swap">
<style>
  :root {
    --teal: #2a9fb8;
    --teal-dark: #1c7f96;
    --teal-light: #bfe6ef;
    --red: #d4202f;
    --ink: #1d2a3a;
    --grey: #6c7178;
    --paper: #ffffff;
    --muscle-light: #eeeeee;
    --muscle-mid: #c9c9c9;
  }
  * { margin: 0; padding: 0; box-sizing: border-box; }
  html, body { width: 849px; height: 1200px; overflow: hidden; background: var(--paper); }
  .poster { position: relative; width: 849px; height: 1200px; overflow: hidden; background: var(--paper); font-family: "PT Serif", Georgia, serif; }

  .anatomy-art {
    position: absolute; left: 0; top: 0; width: 849px; height: 760px;
    background:
      radial-gradient(ellipse 300px 380px at 420px 480px, var(--muscle-mid), transparent 70%),
      radial-gradient(ellipse 260px 200px at 120px 100px, #d6d6d6, transparent 70%),
      linear-gradient(180deg, var(--muscle-light), #e2e2e2);
  }
  .shapes { position: absolute; left: 0; top: 0; }

  .tagline {
    position: absolute; right: 34px; top: 18px;
    font-style: italic; font-size: 56px; color: var(--grey); letter-spacing: 0.5px;
  }
  .tagline .accent { color: var(--red); }

  .brand { position: absolute; left: 28px; top: 165px; display: flex; align-items: center; gap: 22px; }
  .brand-dot { width: 120px; height: 120px; border-radius: 50%; background: var(--paper); opacity: 0.9; }
  .brand-name { font-family: "Open Sans", Arial, sans-serif; font-weight: 700; font-size: 40px; color: var(--paper); }

  .prices-title { position: absolute; left: 690px; top: 432px; font-style: italic; font-size: 38px; color: var(--red); }
  .price { position: absolute; width: 72px; height: 72px; border-radius: 50%; background: var(--teal); border: 4px solid var(--teal-light);
    color: var(--paper); font-weight: 700; font-size: 30px; display: flex; align-items: center; justify-content: center; }
  .price-30 { left: 758px; top: 492px; }
  .price-60 { left: 720px; top: 580px; }
  .price-80 { left: 656px; top: 680px; width: 86px; height: 86px; font-size: 36px; }
  .duration { position: absolute; font-weight: 700; font-size: 18px; color: var(--ink); }
  .duration-30 { left: 650px; top: 550px; }
  .duration-60 { left: 596px; top: 648px; }
  .duration-80 { left: 530px; top: 752px; }

  .services { position: absolute; left: 0; top: 735px; width: 420px; text-align: center; list-style: none; }
  .services li { font-weight: 700; font-size: 45px; line-height: 62px; color: var(--teal-dark); }
  .services .accent { color: var(--red); }

  .contact { position: absolute; left: 510px; top: 790px; color: var(--ink); }
  .contact .phone { font-size: 34px; margin-bottom: 30px; }
  .contact .therapist { font-weight: 700; font-size: 34px; }
  .contact .qualification { font-size: 29px; line-height: 40px; margin-top: 4px; }
  .contact .address { font-size: 29px; line-height: 40px; margin-top: 48px; }
</style>
</head>
<body>
<main class="poster">
  <div class="anatomy-art" role="img" aria-label="Anatomical illustration of a muscular back and arm showing the muscle groups"></div>

  <svg class="shapes" width="849" height="1200" viewBox="0 0 849 1200" aria-hidden="true">
    <path d="M0 0 H849 V115 Q600 95 300 120 Q120 135 0 125 Z" fill="#ffffff"/>
    <path d="M0 150 Q380 115 849 150 V315 Q430 345 0 300 Z" fill="var(--teal)"/>
    <path d="M0 318 Q430 362 849 330" fill="none" stroke="#ffffff" stroke-width="6"/>
    <path d="M0 334 Q430 378 849 346" fill="none" stroke="var(--teal-light)" stroke-width="4"/>
    <path d="M0 700 Q220 640 430 690 Q640 740 849 650 V1200 H0 Z" fill="#ffffff"/>
    <path d="M0 688 Q220 628 430 678 Q640 728 849 638" fill="none" stroke="var(--teal)" stroke-width="9"/>
    <path d="M0 712 Q220 652 430 702 Q640 752 849 662" fill="none" stroke="var(--teal-light)" stroke-width="5"/>
  </svg>

  <p class="tagline">Are you in <span class="accent">pain?</span></p>

  <div class="brand">
    <span class="brand-dot"></span>
    <span class="brand-name">Kneadwell Bodycare</span>
  </div>

  <p class="prices-title">Prices</p>
  <span class="duration duration-30">30 minutes</span>
  <span class="duration duration-60">60 minutes</span>
  <span class="duration duration-80">90 minutes</span>
  <div class="price price-30">$40</div>
  <div class="price price-60">$60</div>
  <div class="price price-80">$80</div>

  <ul class="services">
    <li>Deep Tissue</li>
    <li>Sports <span class="accent">Massage</span></li>
    <li>Relaxation</li>
    <li>Aroma<span class="accent">therapy</span></li>
    <li>Hot Stones</li>
  </ul>

  <div class="contact">
    <p class="phone">0275550148</p>
    <p class="therapist">Mara Tillson</p>
    <p class="qualification">Bachelor Therapeutic<br>&amp; Sports massage</p>
    <p class="address">18 Orwell St,<br>Invercargill 9810</p>
  </div>
</main>
</body>
</html>
```